Flyer Design for Electrical and Solar Services Company

Website: www.bolvanepower.com.au
Email: solar@bolvanepower.com.au
Contact: Mark Bolvane | Sales & Marketing Manager

Background:
Bolvane Power is a Melbourne based company. We provide electrical and solar services for Residential and Commercial customers.
Our proposition is to provide a competitive price with a prompt and reliable service.
Electricity prices are set to double over the next 3 years. This makes Solar a viable option for most Australian households. The right sized solar system will significantly reduce or eliminate an average houses holds electricity bill. We can help customers with a tailored solar system to ensure they get their return on investment.
Our solar package is pitched towards budget conscious houses that are concerned about rising energy costs.

Your task:
Create a double sided flyer for mailbox drops. Size is A4.
Please source a Monocrystalline solar panel and inverter image for this flyer. They can be in the same image.
The flyer must be professional and in line with our website brand and colour scheme (please get logos off the website). It must have a key focus on our solar systems and the great price on offer.

Please refer to uploaded file for the design brief.
Updates

Design brief now uploaded. Hope to hear from you soon, good luck!

Reason: Need more time to review and allow for re-submissions.

Industry/Entity Type

Electrical

Requirements
Must have
• Refer to uploaded file for design brief.

```html
<!DOCTYPE html>
<html lang="en">
<head>
<meta charset="utf-8">
<title>Bolvane Power – Solar Flyer</title>
<link rel="stylesheet" href="https://fonts.googleapis.com/css2?family=Archivo:wght@700;800&family=Arimo:wght@400;700&display=swap">
<style>
:root{
  --navy:#1c3a78;
  --navy-deep:#10275a;
  --blue:#1f5fb0;
  --cyan:#5ec4f0;
  --yellow:#ffd21a;
  --amber:#f6a800;
  --ink:#222;
  --grey:#555;
  --row-a:#dcdfe4;
  --row-b:#eceef1;
  --white:#fff;
}
*{box-sizing:border-box;margin:0;padding:0}
html,body{width:1200px;height:900px;overflow:hidden;background:var(--white);font-family:"Arimo",Arial,sans-serif;color:var(--ink)}
.sheet{position:relative;width:1200px;height:900px}
.page{position:absolute;top:15px;width:567px;height:801px;overflow:hidden}
.front{left:13px;background:linear-gradient(180deg,var(--blue) 45%,var(--navy-deep) 100%)}
.back{left:620px;background:#f7f8fa;border:1px solid #ddd}
.side-label{position:absolute;top:832px;font:700 27px "Arimo",Arial,sans-serif;color:#000}
.abs{position:absolute}

.hero-photo{position:absolute;left:0;top:0;width:567px;height:390px;background:linear-gradient(150deg,#3a4250 0%,#5f7890 35%,#8fc0ea 60%,#cfe6fb 80%,#6ea8dc 100%)}
.hero-curve{position:absolute;left:0;top:330px}

.brand{position:absolute;top:0;width:247px;height:85px;background:var(--navy);border-top:6px solid var(--yellow);color:var(--white);padding:14px 0 0 14px;display:flex;gap:10px}
.brand-dot{width:38px;height:38px;border-radius:50%;background:var(--yellow);flex:none;margin-top:6px}
.brand-name{font:700 20px "Arimo",Arial,sans-serif;line-height:1.2}
.brand-tag{font-size:12.5px;margin-top:3px}

.headline{position:absolute;left:180px;top:170px;width:380px;text-align:center;font-family:"Archivo",Arial,sans-serif;font-weight:800;text-shadow:0 2px 4px rgba(0,0,0,.45)}
.hl-big{color:var(--yellow);font-size:44px;line-height:1}
.hl-small{color:var(--white);font-size:23px;line-height:1.45}
.hl-right{text-align:right;padding-right:0}

.sub-title{color:var(--cyan);font-weight:700;font-size:13px}
.bullets{list-style:none;font-size:9.6px;line-height:15.4px;color:var(--white)}
.bullets li::before{content:"• ";color:var(--cyan)}
.back .bullets{color:var(--ink);font-size:9.4px;line-height:14.8px}
.back .bullets li::before{color:var(--navy)}

.price-table{position:absolute;left:33px;top:488px;width:347px;border-collapse:collapse;background:#eef1f6;font-size:9px;color:#333;box-shadow:0 1px 3px rgba(0,0,0,.4)}
.price-table th{background:var(--navy);color:var(--white);font-weight:700;height:22px;text-align:center}
.price-table td{text-align:center;height:15.5px}
.price-table tr:nth-child(1) td{padding-top:5px}
.terms{left:392px;top:516px;font-size:6.8px;line-height:9.6px;color:#cfdcf0;font-style:italic}

.offer{font-family:"Archivo",Arial,sans-serif;font-weight:800;color:var(--white);font-size:18px}
.offer b{color:var(--yellow);font-size:24px}

.call{position:absolute;width:176px;height:95px;border-radius:8px;background:linear-gradient(180deg,var(--yellow),var(--amber));padding:9px 11px;color:var(--navy-deep)}
.front .call{box-shadow:0 0 0 5px #0b1f4b}
.back .call{box-shadow:0 0 0 5px var(--white),0 2px 8px 5px rgba(0,0,0,.25)}
.call-lead{font-size:15px;font-weight:700}
.call-phone{font-size:20px;font-weight:700;border-bottom:1px solid var(--navy-deep);padding-bottom:2px}
.call-mail{font-size:11px;font-weight:700;margin-top:3px;line-height:1.2}

.back-grid{position:absolute;inset:0;background:linear-gradient(180deg,#eef1f5,#fbfcfd 60%)}
.intro{left:36px;top:32px;font-size:12.6px;line-height:19px;color:var(--navy)}
.panel-photo{position:absolute;left:92px;top:125px;width:430px;height:255px;border-radius:10px;background:linear-gradient(135deg,#2b2f52,#1a1d3a 60%,#4b4f72);box-shadow:0 8px 14px rgba(0,0,0,.25);border:6px solid #d8dadc;transform:skewX(-4deg)}
.sec-title{color:var(--navy);font-weight:700;font-size:13px}
.spec-table{position:absolute;left:32px;top:420px;width:443px;border-collapse:separate;border-spacing:0 1px;font-size:10px}
.spec-table th{background:var(--navy);color:var(--white);text-align:left;padding-left:12px;width:144px;height:22px;font-weight:700}
.spec-table td{text-align:center;color:#333}
.spec-table tr:nth-child(odd) td{background:var(--row-a)}
.spec-table tr:nth-child(even) td{background:var(--row-b)}
.footnote{left:32px;top:524px;font-size:9px;line-height:13.6px;color:var(--grey)}
.footer{position:absolute;left:0;bottom:0;width:100%;height:38px;background:var(--navy);color:var(--white);font-size:11.5px;text-align:center;line-height:38px}
</style>
</head>
<body>
<main class="sheet">

  <section class="page front">
    <div class="hero-photo" role="img" aria-label="Photo of a monocrystalline solar array against a bright blue sky with sun flare"></div>
    <svg class="hero-curve" width="567" height="70" viewBox="0 0 567 70" aria-hidden="true">
      <path d="M0 58 Q280 5 567 20 L567 70 L0 70Z" fill="#1f5fb0"/>
      <path d="M0 58 Q280 5 567 20" fill="none" stroke="#ffffff" stroke-width="3"/>
    </svg>

    <div class="brand" style="left:277px">
      <span class="brand-dot"></span>
      <div><div class="brand-name">Bolvane Power</div><div class="brand-tag">Electricians you can rely on</div></div>
    </div>

    <h1 class="headline">
      <div class="hl-big">Great Savings</div>
      <div class="hl-small">on Your Electric Bill<br>Invest in</div>
      <div class="hl-big">Solar Energy!</div>
    </h1>

    <h2 class="abs sub-title" style="left:33px;top:383px">190 watt Monocrystalline Panels with High Efficiency Inverter</h2>
    <ul class="abs bullets" style="left:36px;top:400px">
      <li>Designed for Australian Climate</li>
      <li>+-3% Power Tolerance</li>
      <li>17% Cell Efficiency</li>
      <li>Panel Warranty - 5 year product, 25 year performance (10 yr 90%, 2 yr 80%)</li>
      <li>Inverter Warranty - 10 years</li>
    </ul>

    <table class="price-table">
      <tr><th>System</th><th>Panel Configuration</th><th>Inverter</th><th>RRP (inc GST)</th><th>Sale Price (inc GST)</th></tr>
      <tr><td>1.52 kW</td><td>8 x 190 watt</td><td>2 kW</td><td>$4,482</td><td>$2,970</td></tr>
      <tr><td>1.90 kW</td><td>10 x 190 watt</td><td>2 kW</td><td>$6,215</td><td>$5,499</td></tr>
      <tr><td>3.04 kW</td><td>16 x 190 watt</td><td>3 kW</td><td>$9,713</td><td>$8,800</td></tr>
      <tr><td>3.99 kW</td><td>21 x 190 watt</td><td>5 kW</td><td>$13,499</td><td>$11,550</td></tr>
      <tr><td>5.13 kW</td><td>27 x 190 watt</td><td>5 kW</td><td>$16,999</td><td>$13,200</td></tr>
    </table>
    <p class="abs terms">Terms:<br>- Prices are less STCs<br>- Flat roof and double story houses are extra.<br>&nbsp;&nbsp;Call for prices.<br>- Prices based on Melbourne metro location</p>

    <p class="abs offer" style="right:35px;top:606px">Free for the first <b>100</b> customers...</p>
    <p class="abs offer" style="left:36px;top:635px">Voltique Energy Meter RRP <b>$220</b></p>

    <h3 class="abs sub-title" style="left:33px;top:680px">Voltique Energy Meter can:</h3>
    <ul class="abs bullets" style="left:36px;top:698px">
      <li>Show you how much energy your home is using or generating<br>&nbsp;&nbsp;&nbsp;at any given time</li>
      <li>Show your usage in watts or in $$$</li>
      <li>Changes colour when you're using a higher volume of electricity</li>
      <li>This is portable, so you can put this anywhere in the home</li>
    </ul>

    <div class="call" style="left:359px;top:683px">
      <div class="call-lead">Call Now!</div>
      <div class="call-phone">1300 642 915</div>
      <div class="call-mail">Email us:<br>solar@bolvanepower.com.au</div>
    </div>
  </section>

  <section class="page back">
    <div class="back-grid"></div>
    <p class="abs intro">Enjoy the greatest savings on<br>your utility bill over the lifetime of<br>your solar energy system.</p>
    <div class="brand" style="left:283px">
      <span class="brand-dot"></span>
      <div><div class="brand-name">Bolvane Power</div><div class="brand-tag">Electricians you can rely on</div></div>
    </div>

    <div class="panel-photo" role="img" aria-label="Product photo of a single monocrystalline solar panel in a silver frame"></div>

    <h2 class="abs sec-title" style="left:32px;top:396px">System Characteristics</h2>
    <table class="spec-table">
      <tr><th>System size</th><td>1.52 kW</td><td>1.90 kW</td><td>3.04 kW</td><td>3.99 kW</td><td>5.13 kW</td></tr>
      <tr><th>Roof space required</th><td>11 m2</td><td>16 m2</td><td>21 m2</td><td>31 m2</td><td>36 m2</td></tr>
      <tr><th>190W number of panels</th><td>8</td><td>10</td><td>21</td><td>21</td><td>27</td></tr>
      <tr><th>Ave. kWh per day*</th><td>5.4</td><td>7.2</td><td>10.8</td><td>14.4</td><td>18.0</td></tr>
    </table>
    <p class="abs footnote">*Output based on optimal installation direction averaged on an annual basis.<br>&nbsp;Performance varies by location. NSB Solar PV Buyer Guide Vol 5 System,<br>&nbsp;specifications may change without notice.</p>

    <h2 class="abs sec-title" style="left:32px;top:590px">The Benefits:</h2>
    <ul class="abs bullets" style="left:40px;top:608px">
      <li>Panels and Inverter are National Solar Board (NSB) approved</li>
      <li>Quick installation times by licensed and NSB accredited electricians</li>
      <li>Energy prices are set to double over the next 3 years.<br>&nbsp;&nbsp;&nbsp;The right solar system will significantly reduce or<br>&nbsp;&nbsp;&nbsp;eliminate your electricity bills</li>
      <li>No greenhouse gas emissions</li>
      <li>Increased value of your home or business</li>
    </ul>

    <div class="call" style="left:356px;top:640px">
      <div class="call-lead">Call Now!</div>
      <div class="call-phone">1300 642 915</div>
      <div class="call-mail">Email us:<br>solar@bolvanepower.com.au</div>
    </div>

    <footer class="footer">www.bolvanepower.com.au</footer>
  </section>

  <p class="side-label" style="left:13px">FRONT</p>
  <p class="side-label" style="left:621px">BACK</p>
</main>
</body>
</html>
```